BramliVex a new start up looking for packaging design for it's organic Cold pressed Peanut oil.

We require a labelling design for a new company based in the UK called ''BramliVex''. We will be launching Organic cold pressed peanut oil. We would like a design that is simple yet very catchy and not boring.

Target Market(s)
General consumers and healthy eaters, Vegan friendly

Colors
Designer to choose colors to be used in the design.

Must have
• Refer to Packaging document information for labelling.
• Type of bottle 250 ML Selvane bottle (refer to Bottle Picture doc.)
• Must have the "BramliVex" logo stamped somewhere on the front of the package (refer to the Logo document)
• Sleek and appetising design
• Neutral colors possible accents with logo colors
• Claims: Organic, Vegan, High in Monounsaturated fat, High in Poly-unsaturated fat(all this in front of the package)
• Made in the uk logo, and EU organic logo
• Social Media Icons (Pictaloom,Chatterdesk) as well as website (Bramlivex.co.uk)
• Space reserved at the back of the package for barcode and best before date to be printed on.
Be nice to have: picture of the product on the background if possible
Updates

Need extra days to review

Target Market(s)

Font styles to use
Serif
Sans Serif
Decorative
Script

Requirements
Must have

• • Refer to Packaging document information for labelling.

```html
<!DOCTYPE html>
<html lang="en">
<head>
<meta charset="utf-8">
<title>BramliVex Organic Cold Pressed Peanut Oil – Label</title>
<link rel="stylesheet" href="https://fonts.googleapis.com/css2?family=Poppins:wght@500;600;700&family=Roboto+Condensed:wght@400&display=swap">
<style>
  :root {
    --bg: #2b2a27;
    --label-white: #ffffff;
    --brown: #5b2b14;
    --orange: #e9842c;
    --green: #8cc63f;
    --photo-light: #ecd7b0;
    --photo-mid: #d9a96c;
    --claim-line: #ffffff;
  }
  * { box-sizing: border-box; margin: 0; padding: 0; }
  html, body { width: 1200px; height: 1000px; overflow: hidden; }
  body {
    background: var(--bg);
    display: flex;
    align-items: center;
    justify-content: center;
    font-family: "Poppins", sans-serif;
  }
  .label {
    position: relative;
    width: 330px;
    height: 930px;
    background: var(--label-white);
    overflow: hidden;
  }
  .label__band {
    position: absolute;
    left: 0; top: 0;
    width: 100%; height: 100%;
  }
  .brand {
    position: absolute;
    top: 118px; left: 0; width: 100%;
    display: flex; flex-direction: column; align-items: center; gap: 8px;
  }
  .brand__dot {
    width: 14px; height: 14px; border-radius: 50%;
    background: var(--brown);
  }
  .brand__name {
    font-weight: 600;
    font-size: 28px;
    line-height: 1;
    color: var(--brown);
  }
  .badge-organic {
    position: absolute;
    top: 266px; left: 50%; transform: translateX(-50%);
    background: var(--green);
    color: #fff;
    font-family: "Roboto Condensed", sans-serif;
    font-size: 14px;
    line-height: 20px;
    padding: 0 13px;
    border-radius: 10px;
  }
  .title {
    position: absolute;
    top: 300px; left: 0; width: 100%;
    text-align: center;
    color: var(--brown);
  }
  .title__sub {
    display: block;
    font-weight: 600;
    font-size: 24px;
    line-height: 30px;
  }
  .title__main {
    display: block;
    font-weight: 700;
    font-size: 42px;
    line-height: 50px;
  }
  .title__accent { color: var(--orange); }
  .product-photo {
    position: absolute;
    top: 400px; left: 80px;
    width: 170px; height: 250px;
    border-radius: 16px;
    background: radial-gradient(ellipse at 50% 65%, var(--photo-light) 0%, var(--photo-mid) 100%);
  }
  .claims {
    position: absolute;
    top: 672px; left: 0; width: 100%;
    list-style: none;
    display: flex; flex-direction: column; align-items: center; gap: 14px;
  }
  .claims__item {
    width: 214px;
    height: 30px;
    line-height: 27px;
    border: 1.5px solid var(--claim-line);
    border-radius: 15px;
    color: #fff;
    text-align: center;
    font-family: "Roboto Condensed", sans-serif;
    font-size: 12px;
  }
  .volume {
    position: absolute;
    top: 872px; left: 0; width: 100%;
    text-align: center;
    color: #fff;
    font-family: "Roboto Condensed", sans-serif;
    font-size: 13px;
  }
</style>
</head>
<body>
  <main class="label">
    <svg class="label__band" viewBox="0 0 330 930" preserveAspectRatio="none" aria-hidden="true">
      <defs>
        <linearGradient id="band-fill" x1="0" y1="0" x2="0" y2="1">
          <stop offset="0" stop-color="#e27d28"/>
          <stop offset="1" stop-color="#f29a42"/>
        </linearGradient>
      </defs>
      <path d="M0 588 C 90 570, 200 558, 330 552 L330 930 L0 930 Z" fill="url(#band-fill)"/>
    </svg>

    <div class="brand">
      <span class="brand__dot"></span>
      <span class="brand__name">BramliVex</span>
    </div>

    <span class="badge-organic">ORGANIC</span>

    <h1 class="title">
      <span class="title__sub">COLD PRESSED</span>
      <span class="title__main">PEANUT <span class="title__accent">OIL</span></span>
    </h1>

    <div class="product-photo" role="img" aria-label="Photo of whole and shelled peanuts with a green leaf"></div>

    <ul class="claims">
      <li class="claims__item">ORGANIC</li>
      <li class="claims__item">VEGAN</li>
      <li class="claims__item">HIGH IN POLY-UNSATURATED FAT</li>
      <li class="claims__item">HIGH IN POLY-UNSATURATED FAT</li>
    </ul>

    <p class="volume">250 ML</p>
  </main>
</body>
</html>
```